120ml Jar Label — Masculine Cosmetic Foot Balm for Cracked, Hardworking Heels

We need a print-ready wraparound label for a 120ml jar — a brown/amber glass jar with a black metal screw lid (file photo attached).

--DO NOT PUT A BARCODE ON THE LABEL PLEASE--
**PLEASE READ "PLAN HUDDLE PROJECT BRIEF FINAL.MD" IN ATTACHED FILES IF YOU ARE SUBMITTING A DESIGN.**

The label is 190mm wide × 40mm high.
We need files to be in an .ai format with a 2mm bleed at the end.
Social media handle: @bramblekeepnz (facebook, instagram and tiktok)

Bramble Keep is a New Zealand foot-care brand making practical, no-nonsense products for hardworking men whose jobs wreck their feet. Our flagship product, Ridge Mender Balm, helps fix thick, cracked, hardworking skin.

Brand color scheme and overview is all in the brief file. You may add some brand aligned colors outside of the specified hex codes as you see fit to make a great design. Feel free to remove the "Bramble Keep" text from the logo so Bramble Keep is not doubled up on the front of the label

The tone we want: direct, rugged, and credible — like a workwear brand, not a spa brand. Most cracked-heel products on the market lean soft and feminine; we want to stand apart by looking like a serious fix for a real problem, made in New Zealand.

Full legal requirements for New Zealand cosmetic labelling (ingredients, directions, net contents, origin, etc.) are listed in the attached brief document — these are non-negotiable and must stay legible.

Please see the label attached "Label spacing guide" for this project's rough spacing guide. This label is the same size and sits well on the jar. This label doesn't need to be spaced quite as much as the Verin Label

I want to run the design for a week - I feel 7 days is a good amount of time for designers to see the work, digest the brief and create something remarkable and memorable for Bramble Keep.

Target Market(s)

Working men in New Zealand whose jobs or lifestyle put heavy wear on their feet — tradies, farmers, hospital/shift workers, hunters, and outdoors people. Practical, value-driven buyers rather than luxury skincare shoppers.

Industry/Entity Type

Beauty / Health & Wellness / Cosmetics

Font styles to use
Sans Serif
Other font styles liked:
• Montserrat (bold, headings), Inter (regular, body)

Colors
00AB8E
00BBA5
67D7C9
C6EFE9
E9F9F6
FFC000
F8CF3A
FAE287
FDF2CF
FEFAEE

Requirements
Must have
• All NZ cosmetic labelling requirements from the attached brief (product name, tag line, net contents, ingredients, directions, storage, made in NZ) — legible and complete, not omitted for aesthetics Fits 190mm × 40mm wraparound format for a 120ml brown jar with black lid Uses our existing brand colors: Deep Olive #3C4A34, Bone White #F4EFE6, Terracotta Clay #C1683D, and Warm Grey #4A4540 (exact palette in attached brief) Uses Montserrat (headings) and Inter (body) or close equivalents Incorporates our existing shield-and-wing logo (attached) Brand name and product name clearly readable from a normal shelf/bathroom-cabinet distance
Nice to have
• A style that could extend into a hero/product photo later, similar to the NZ-hills-backdrop look on our website (screenshot attached) — not required for the label itself, just good to keep in mind Original icon work (e.g. a small soak/apply/sock icon set) if it fits the rugged brand feel A design that could work as a small back-label/wraparound split if the front can't fit everything at a readable size
Should not have
• No pastel colors, floral motifs, or delicate script fonts — this should never look like spa/luxury skincare. Don't introduce new brand colors outside the palette provided other than black.

```html
<!DOCTYPE html>
<html lang="en">
<head>
<meta charset="utf-8">
<title>Ridge Mender Balm – Label Options</title>
<link href="https://fonts.googleapis.com/css2?family=Archivo+Black&family=Barlow+Condensed:wght@500;600;700;800&family=Barlow+Semi+Condensed:wght@400;500;600&family=Montserrat:wght@700;800&display=swap" rel="stylesheet">
<style>
  :root {
    --ink: #23241f;
    --cream: #f7e6cc;
    --cream-soft: #fbeedd;
    --terracotta: #b8694a;
    --terracotta-text: #c97a55;
    --olive: #3c4431;
    --olive-deep: #333b2a;
    --rust: #b14a2e;
    --rust-text: #c85a36;
    --bone: #f0eadd;
    --mountain: #4a4a3a;
  }
  * { margin: 0; padding: 0; box-sizing: border-box; }
  html, body { width: 1200px; height: 651px; overflow: hidden; background: #fff; }
  body { position: relative; font-family: "Barlow Semi Condensed", sans-serif; }
  .abs { position: absolute; }

  .option-title {
    position: absolute; left: 59px;
    font-family: "Montserrat", sans-serif; font-weight: 800;
    font-size: 26px; letter-spacing: 2px; color: var(--rust);
  }

  /* ---------- Option 1 ---------- */
  .label-one {
    position: absolute; left: 59px; top: 54px; width: 1090px; height: 250px;
    background: var(--cream); border-radius: 6px; overflow: hidden;
  }
  .label-one .body {
    position: absolute; left: 0; top: 9px; width: 1090px; height: 235px;
    background: var(--ink);
  }
  .one-kicker {
    left: 49px; top: 17px; font-family: "Barlow Semi Condensed", sans-serif;
    font-weight: 600; font-size: 13.5px; line-height: 16px; color: var(--terracotta-text);
  }
  .one-intro {
    left: 47px; top: 55px; width: 200px; font-size: 11.6px; line-height: 13.2px;
    color: var(--cream);
  }
  .benefit { left: 50px; display: flex; align-items: center; gap: 8px; }
  .benefit svg { width: 17px; height: 17px; flex: none; }
  .benefit p { font-size: 10.6px; line-height: 11.6px; color: var(--cream); font-weight: 500; }
  .benefit b { font-weight: 500; text-transform: uppercase; display: block; }

  .one-emblem {
    left: 286px; top: 22px; width: 160px; height: 178px; border-radius: 18px 18px 80px 80px;
    background: linear-gradient(135deg, var(--cream) 0%, #d7a784 50%, var(--terracotta) 100%);
  }
  .one-divider { left: 464px; top: 16px; width: 1px; height: 200px; background: var(--cream); opacity: .7; }

  .one-mountains {
    left: 640px; top: 95px; width: 343px; height: 140px;
    background: linear-gradient(180deg, rgba(74,74,58,0) 0%, rgba(74,74,58,.55) 55%, rgba(74,74,58,.7) 100%);
  }
  .one-name {
    left: 486px; top: 16px; font-family: "Archivo Black", sans-serif;
    color: var(--cream); line-height: .8;
  }
  .one-name .l1 { font-size: 58px; letter-spacing: -1px; display: block; }
  .one-name .l2 { font-size: 58px; letter-spacing: -2px; display: block; margin-top: 8px; }
  .one-name .l3 { font-size: 50px; letter-spacing: -1px; display: block; margin-top: 10px; color: var(--terracotta); }
  .one-tagbox {
    left: 486px; top: 174px; width: 236px; height: 20px; background: var(--cream);
    font-family: "Barlow Condensed", sans-serif; font-weight: 700; font-size: 16px;
    color: var(--ink); display: flex; align-items: center; justify-content: center; gap: 7px;
    letter-spacing: .3px;
  }
  .one-use {
    left: 486px; top: 203px; font-family: "Barlow Condensed", sans-serif; font-weight: 600;
    font-size: 17px; color: var(--cream); letter-spacing: .2px;
  }
  .one-origin {
    left: 820px; top: 35px; width: 103px; text-align: right;
    font-family: "Barlow Condensed", sans-serif; font-weight: 700; font-size: 16px;
    line-height: 15.5px; color: var(--cream);
  }
  .one-origin-rule { left: 834px; top: 70px; width: 89px; height: 2px; background: var(--terracotta); }
  .one-fern {
    left: 926px; top: 28px; width: 38px; height: 46px; border-radius: 40% 5% 40% 5%;
    background: linear-gradient(45deg, #e7d6bb, var(--cream));
    transform: rotate(-10deg);
  }
  .one-volume {
    left: 845px; top: 180px; width: 107px; text-align: right; color: var(--cream);
    font-family: "Barlow Condensed", sans-serif;
  }
  .one-volume .ml { font-weight: 700; font-size: 24px; line-height: 24px; display: block; }
  .one-volume .oz { font-weight: 500; font-size: 14.5px; line-height: 16px; display: block; }

  .one-steps {
    left: 983px; top: 0; width: 79px; height: 235px; background: var(--terracotta);
  }
  .one-step { position: absolute; left: 0; width: 79px; text-align: center; }
  .one-step .ring {
    width: 46px; height: 46px; margin: 0 auto; border-radius: 50%;
    border: 1.6px solid var(--cream); background: rgba(247,230,204,.15);
  }
  .one-step span {
    display: block; margin-top: 4px; font-family: "Barlow Condensed", sans-serif;
    font-weight: 700; font-size: 12.5px; color: var(--cream); letter-spacing: .3px;
  }

  /* ---------- Option 2 ---------- */
  .label-two {
    position: absolute; left: 59px; top: 370px; width: 1090px; height: 250px;
    background: var(--olive); border-radius: 7px; overflow: hidden;
  }
  .two-kicker {
    left: 44px; top: 28px; font-family: "Barlow Condensed", sans-serif; font-weight: 600;
    font-size: 14.5px; color: var(--rust-text); letter-spacing: .2px;
  }
  .two-intro {
    left: 44px; top: 47px; width: 195px; font-size: 12.6px; line-height: 15.2px;
    color: var(--cream-soft);
  }
  .two-rule { left: 44px; top: 132px; width: 190px; height: 1px; background: var(--rust-text); }
  .two-step { position: absolute; top: 146px; width: 68px; text-align: center; color: var(--cream-soft); }
  .two-step .glyph {
    width: 40px; height: 38px; margin: 0 auto; border-radius: 8px;
    background: linear-gradient(180deg, rgba(240,234,221,.35), rgba(240,234,221,.15));
  }
  .two-step h4 {
    margin-top: 7px; font-family: "Barlow Condensed", sans-serif; font-weight: 600;
    font-size: 15.5px; color: var(--rust-text); letter-spacing: .3px; line-height: 16px;
  }
  .two-step p { font-size: 9.6px; line-height: 11.4px; margin-top: 4px; }
  .two-step-rule { top: 169px; width: 1px; height: 62px; background: var(--rust-text); }

  .two-band { left: 377px; top: 17px; width: 333px; height: 161px; background: var(--bone); }
  .two-band-rust { left: 349px; top: 176px; width: 361px; height: 31px; background: var(--rust); }
  .two-emblem {
    left: 255px; top: 15px; width: 176px; height: 197px; border-radius: 20px 20px 90px 90px;
    background: linear-gradient(150deg, var(--bone) 0%, #c9c4b4 45%, var(--olive-deep) 100%);
    border: 5px solid var(--bone);
  }
  .two-name {
    left: 436px; top: 30px; font-family: "Archivo Black", sans-serif; font-size: 74px;
    line-height: 74px; letter-spacing: -2px; color: var(--olive-deep);
  }
  .two-sub {
    left: 437px; top: 111px; font-family: "Barlow Condensed", sans-serif; font-weight: 800;
    font-size: 42px; line-height: 40px; color: var(--rust); letter-spacing: -.3px;
  }
  .two-tag {
    left: 437px; top: 154px; font-family: "Barlow Condensed", sans-serif; font-weight: 700;
    font-size: 17px; color: var(--olive-deep); letter-spacing: .5px;
  }
  .two-use {
    left: 437px; top: 182px; font-family: "Barlow Condensed", sans-serif; font-weight: 600;
    font-size: 17.5px; color: var(--bone); letter-spacing: .5px;
  }
  .two-volume {
    left: 376px; top: 218px; display: flex; align-items: center; gap: 9px;
    font-family: "Barlow Condensed", sans-serif; color: var(--cream-soft);
  }
  .two-volume .qty { font-size: 15px; font-weight: 500; }
  .two-volume .fern {
    width: 34px; height: 11px; border-radius: 50% 10% 50% 10%;
    background: linear-gradient(90deg, #d8d2c2, var(--bone)); transform: rotate(-18deg);
  }
  .two-volume .origin { font-size: 12.5px; font-weight: 600; letter-spacing: .3px; }

  .two-legal { left: 723px; top: 33px; width: 218px; color: var(--cream-soft); font-size: 10.2px; line-height: 12.2px; }
  .two-legal .head { color: var(--rust-text); font-family: "Barlow Condensed", sans-serif; font-weight: 600; }
  .two-legal .block { margin-bottom: 12px; }
  .two-legal .justify { text-align: justify; }
  .two-legal hr { border: 0; height: 1px; background: var(--rust-text); margin: 0 0 12px; width: 211px; }
  .two-legal .made { color: var(--rust-text); font-size: 12.5px; margin-top: 22px; font-family: "Barlow Semi Condensed", sans-serif; }

  .two-brand {
    left: 949px; top: 0; width: 129px; height: 250px; background: var(--bone);
    text-align: center; color: var(--olive-deep);
  }
  .two-brand .mark {
    width: 40px; height: 40px; margin: 24px auto 0; border-radius: 50%; background: var(--olive-deep);
  }
  .two-brand .mark-name {
    margin-top: 7px; font-family: "Barlow Condensed", sans-serif; font-weight: 700;
    font-size: 13px; letter-spacing: .3px;
  }
  .two-brand .company {
    margin-top: 20px; font-family: "Barlow Condensed", sans-serif; font-weight: 700; font-size: 13.5px;
  }
  .two-brand .kiwi { font-size: 10.2px; line-height: 12.4px; margin-top: 1px; }
  .two-brand .rule { width: 82px; height: 1px; background: var(--rust-text); margin: 11px auto 14px; }
  .two-brand .handle { font-size: 11px; font-weight: 600; }
  .two-brand .web { font-size: 11px; font-weight: 600; margin-top: 13px; }
  .label-two .edge { position: absolute; left: 1078px; top: 0; width: 12px; height: 250px; background: var(--olive); }
</style>
</head>
<body>

  <h2 class="option-title" style="top:20px;">OPTION - 1</h2>

  <section class="label-one">
    <div class="body">
      <p class="abs one-kicker">MADE FOR HARD FEET.<br>BUILT TO WORK.</p>
      <p class="abs one-intro">Bramble Keep Ridge Mender Balm is a deep-conditioning formula that helps repair thick, cracked skin and restores softness where other balms fail.</p>

      <div class="abs benefit" style="top:124px;">
        <svg viewBox="0 0 20 20"><circle cx="10" cy="10" r="10" fill="#f7e6cc"/><path d="M5.5 10.3l3 3 6-6.4" stroke="#23241f" stroke-width="2.4" fill="none" stroke-linecap="round" stroke-linejoin="round"/></svg>
        <p><b>Softens &amp; repairs</b>thick, cracked heels</p>
      </div>
      <div class="abs benefit" style="top:158px;">
        <svg viewBox="0 0 20 20"><circle cx="10" cy="10" r="10" fill="#f7e6cc"/><path d="M5.5 10.3l3 3 6-6.4" stroke="#23241f" stroke-width="2.4" fill="none" stroke-linecap="round" stroke-linejoin="round"/></svg>
        <p><b>Deeply hydrates</b>dry, rough skin</p>
      </div>
      <div class="abs benefit" style="top:192px;">
        <svg viewBox="0 0 20 20"><circle cx="10" cy="10" r="10" fill="#f7e6cc"/><path d="M5.5 10.3l3 3 6-6.4" stroke="#23241f" stroke-width="2.4" fill="none" stroke-linecap="round" stroke-linejoin="round"/></svg>
        <p><b>Works hard</b>so you can keep going</p>
      </div>

      <div class="abs one-emblem" role="img" aria-label="Shield emblem with a foot and fern frond"></div>
      <div class="abs one-divider"></div>

      <div class="abs one-mountains" role="img" aria-label="New Zealand mountain range backdrop"></div>

      <h1 class="abs one-name"><span class="l1">RIDGE</span><span class="l2">MENDER</span><span class="l3">BALM</span></h1>
      <div class="abs one-tagbox"><span>REPAIR</span><span>•</span><span>SOFTEN</span><span>•</span><span>PROTECT</span></div>
      <p class="abs one-use">FOR CRACKED, HARDWORKING HEELS</p>

      <p class="abs one-origin">MADE IN<br>NEW ZEALAND</p>
      <div class="abs one-origin-rule"></div>
      <div class="abs one-fern" role="img" aria-label="Silver fern frond"></div>

      <p class="abs one-volume"><span class="ml">120ml ℮</span><span class="oz">4.06 fl oz</span></p>

      <div class="abs one-steps">
        <div class="one-step" style="top:18px;"><div class="ring" role="img" aria-label="Foot soaking in water icon"></div><span>SOAK</span></div>
        <div class="one-step" style="top:91px;"><div class="ring" role="img" aria-label="Hand applying balm to foot icon"></div><span>APPLY</span></div>
        <div class="one-step" style="top:163px;"><div class="ring" role="img" aria-label="Sock icon"></div><span>PROTECT</span></div>
      </div>
    </div>
  </section>

  <h2 class="option-title" style="top:336px;">OPTION -2</h2>

  <section class="label-two">
    <p class="abs two-kicker">BUILT FOR HARDWORKING FEET</p>
    <p class="abs two-intro">Ridge Mender Balm is a no-nonsense formula that helps repair dry, cracked heels and tough, calloused skin. Made in New Zealand with premium ingredients that work.</p>
    <div class="abs two-rule"></div>

    <div class="two-step" style="left:34px;"><div class="glyph" role="img" aria-label="Foot in basin icon"></div><h4>SOAK</h4><p>Soak feet in<br>warm water</p></div>
    <div class="abs two-step-rule" style="left:101px;"></div>
    <div class="two-step" style="left:102px;"><div class="glyph" role="img" aria-label="Hand massaging heel icon"></div><h4>APPLY</h4><p>Massage balm<br>into heels</p></div>
    <div class="abs two-step-rule" style="left:172px;"></div>
    <div class="two-step" style="left:173px;"><div class="glyph" role="img" aria-label="Sock icon"></div><h4>SOCKS</h4><p>Wear socks<br>overnight</p></div>

    <div class="abs two-band"></div>
    <div class="abs two-band-rust"></div>
    <div class="abs two-emblem" role="img" aria-label="Riveted shield emblem with a foot and fern frond"></div>

    <h1 class="abs two-name">RIDGE</h1>
    <p class="abs two-sub">MENDER BALM</p>
    <p class="abs two-tag">FIX. FORTIFY.&nbsp; GET BACK TO WORK.</p>
    <p class="abs two-use">FOR CRACKED, HARDWORKING HEELS</p>

    <div class="abs two-volume">
      <span class="qty">120ml ℮ 4.06 fl oz</span>
      <span class="fern" role="img" aria-label="Silver fern frond"></span>
      <span class="origin">MADE IN NEW ZEALAND</span>
    </div>

    <div class="abs two-legal">
      <p class="block"><span class="head">DIRECTIONS:</span> Soak feet in warm water. Dry thoroughly. Massage a generous amount into heels. For results, use nightly and wear socks.</p>
      <hr>
      <p class="block justify"><span class="head">INGREDIENTS:</span> Shea Butter, Beef Tallow, Beeswax, Grape Seed Oil, Vegetable Glycerin, Lanolin, Panthenol, Gluconolactone, Sodium Benzoate, Allantoin, Manuka Honey, Vitamin E, Tea Tree Essential Oil, Lemon Myrtle Essential Oil, Rosemary Oleoresin Extract</p>
      <hr>
      <p><span class="head">STORAGE:</span> Store below 25C in a cool, dry place.<br>Keep out of direct sunlight.</p>
      <p class="made">Made in New Zealand</p>
    </div>

    <div class="abs two-brand">
      <div class="mark"></div>
      <p class="mark-name">BRAMBLE KEEP</p>
      <p class="company">BRAMBLE KEEP NZ</p>
      <p class="kiwi">Proudly made for<br>hardworking Kiwis.</p>
      <div class="rule"></div>
      <p class="handle">@bramblekeepnz</p>
      <p class="web">www.bramblekeep.nz</p>
    </div>
    <div class="edge"></div>
  </section>

</body>
</html>
```